Ferro Vale Hydration Product that supports healthy blood pressure and Hydration

Design Brief: Hydration Product for Blood Pressure Support
Product Name: "47" or "Velora"
We are developing a hydration product aimed at supporting healthy blood pressure while keeping users hydrated. The product will have a clinical, clean, and functional design, and we're looking for a professional designer or team to bring this vision to life.

Project Overview
We want a product design (logo, label, and possibly packaging) that communicates:

Hydration

Blood pressure support

Pharmaceutical/medical Look

Health and wellness

This product will be used by health-conscious consumers and individuals managing their blood pressure.

Design Objectives
Reflect both hydration and blood pressure support visually.

Appeal to a clinical, trustworthy, yet fresh and modern aesthetic.

Clearly communicate functionality and health benefits.

Visual Elements to Consider
We would like to explore the use of the following visual motifs:

Water drop – to symbolize hydration

Blood drop – to signify blood pressure support

Medical or pharmaceutical elements – cross, heartbeat/EKG lines, capsules, etc.

Typography – Clean, sans-serif fonts; professional and modern

Color Preferences
We have attached reference images showing preferred color schemes. These are mostly in the blue, red, and white family (for hydration, blood, and clinical cleanliness).

However, we are open to other colors that you feel will enhance the brand’s purpose.

Target Market(s)

Hydration

Industry/Entity Type

Health and Wellness

Font styles to use
Serif
Sans Serif
Decorative
Script

Colors
00AB8E
00BBA5
67D7C9
C6EFE9
E9F9F6

Requirements
Must have
• design that incorporates a clean pharmaceutical look and refreshing design
Nice to have
• Medica look
Should not have
• Clean Design. Silver and Cobalt Blue Design as an additional

```html
<!DOCTYPE html>
<html lang="en">
<head>
<meta charset="utf-8">
<title>Velora Stick Pack</title>
<link rel="stylesheet" href="https://fonts.googleapis.com/css2?family=Josefin+Sans:wght@700&family=Quicksand:wght@400&display=swap">
<style>
  :root {
    --bg: #ece9e6;
    --wrap-red: #c8252f;
    --wrap-red-dark: #a81b24;
    --label: #eef5f1;
    --label-shade: #dfe9e4;
    --brand-blue: #1f5f8b;
    --water-blue: #5fb6d8;
    --ink: #3a3a3a;
    --icon: #1b1b1b;
  }
  * { box-sizing: border-box; margin: 0; padding: 0; }
  html, body { width: 1200px; height: 1200px; overflow: hidden; background: var(--bg); }
  .canvas { position: relative; width: 1200px; height: 1200px; }

  .stick-pack {
    position: absolute; top: 90px; width: 300px; height: 1020px;
    display: flex; flex-direction: column;
    box-shadow: 0 18px 40px rgba(0,0,0,.18);
  }
  .stick-pack--front { left: 190px; }
  .stick-pack--back { left: 710px; }

  .crimp {
    height: 150px; flex: none;
    background: linear-gradient(90deg, var(--wrap-red-dark), var(--wrap-red) 30%, var(--wrap-red) 70%, var(--wrap-red-dark));
    position: relative;
  }
  .crimp::after {
    content: ""; position: absolute; left: 0; right: 0; height: 4px;
    background: rgba(0,0,0,.12);
  }
  .crimp--top::after { top: 28px; }
  .crimp--bottom::after { bottom: 28px; }

  .label {
    flex: 1; position: relative; overflow: hidden;
    background: linear-gradient(90deg, var(--label-shade), var(--label) 40%, var(--label));
  }

  .vertical {
    position: absolute;
    writing-mode: vertical-rl;
    white-space: nowrap;
    line-height: 1;
  }

  /* front */
  .brand-dot {
    position: absolute; top: 30px; left: 150px;
    width: 80px; height: 80px; border-radius: 50%;
    background: var(--water-blue);
  }
  .seal-badge {
    position: absolute; top: 125px; left: 200px;
    width: 36px; height: 36px; border-radius: 50%;
    border: 3px solid var(--wrap-red);
  }
  .brand-name {
    top: 185px; right: 34px;
    font-family: "Josefin Sans", sans-serif; font-weight: 700;
    font-size: 100px; letter-spacing: 4px;
    color: var(--brand-blue);
  }
  .tagline {
    top: 150px; right: 150px;
    font-family: "Quicksand", sans-serif; font-weight: 400;
    font-size: 24px; color: var(--ink);
  }
  .front-lorem {
    top: 90px; right: 192px;
    font-family: "Quicksand", sans-serif; font-weight: 400;
    font-size: 20px; color: var(--ink);
  }

  /* back */
  .seam {
    position: absolute; top: 0; bottom: 0; left: 92px; width: 2px;
    background: rgba(0,0,0,.08);
  }
  .back-copy {
    position: absolute; top: 24px; right: 30px; height: 400px;
    writing-mode: vertical-rl;
    font-family: "Quicksand", sans-serif; font-size: 20px; line-height: 1.3;
    color: var(--ink);
  }
  .info-icons {
    position: absolute; bottom: 30px; right: 44px;
    display: flex; flex-direction: column; gap: 16px; align-items: center;
  }
  .info-icons svg { display: block; }
</style>
</head>
<body>
<main class="canvas">

  <section class="stick-pack stick-pack--front" aria-label="Velora stick pack, front">
    <div class="crimp crimp--top"></div>
    <div class="label">
      <span class="brand-dot"></span>
      <span class="seal-badge"></span>
      <h1 class="vertical brand-name">VELORA</h1>
      <p class="vertical tagline">blood pressure and hydration support</p>
      <p class="vertical front-lorem">Lorem ipsum dolor sit amet, consectetuer</p>
    </div>
    <div class="crimp crimp--bottom"></div>
  </section>

  <section class="stick-pack stick-pack--back" aria-label="Velora stick pack, back">
    <div class="crimp crimp--top"></div>
    <div class="label">
      <span class="seam"></span>
      <p class="back-copy">Lorem ipsum dolor sit amet, Lorem ipsum dolor sit amet, consectetuer adipiscing elit, sed diam nonummy nibh euismod tincidunt ut laoreet dolore magna</p>
      <div class="info-icons">
        <svg width="44" height="44" viewBox="0 0 50 50" aria-label="not for children">
          <circle cx="25" cy="25" r="21" fill="none" stroke="var(--icon)" stroke-width="4"/>
          <rect x="18" y="14" width="14" height="20" rx="3" fill="var(--icon)"/>
          <line x1="10" y1="10" x2="40" y2="40" stroke="var(--icon)" stroke-width="4"/>
        </svg>
        <svg width="44" height="44" viewBox="0 0 50 50" aria-label="gluten free">
          <circle cx="25" cy="25" r="21" fill="none" stroke="var(--icon)" stroke-width="4"/>
          <line x1="25" y1="12" x2="25" y2="38" stroke="var(--icon)" stroke-width="2"/>
          <line x1="10" y1="10" x2="40" y2="40" stroke="var(--icon)" stroke-width="4"/>
        </svg>
        <svg width="44" height="44" viewBox="0 0 50 50" aria-label="recyclable">
          <circle cx="25" cy="25" r="22" fill="var(--icon)"/>
          <path d="M14 25a11 11 0 0 1 19-7" fill="none" stroke="#fff" stroke-width="4"/>
          <path d="M36 25a11 11 0 0 1-19 7" fill="none" stroke="#fff" stroke-width="4"/>
        </svg>
        <svg width="44" height="44" viewBox="0 0 50 50" aria-label="dispose in bin">
          <rect x="4" y="4" width="42" height="42" fill="none" stroke="var(--icon)" stroke-width="3"/>
          <rect x="19" y="12" width="14" height="18" fill="none" stroke="var(--icon)" stroke-width="2"/>
        </svg>
      </div>
    </div>
    <div class="crimp crimp--bottom"></div>
  </section>

</main>
</body>
</html>
```